Exercise Physiologist needs business cards

I have a logo, I need business cards (Sole trader) as I am moving to a new location and would like an updated look. I provide gym based exercise rehabilitation, injury prevention and movement assessments. I have over 13 years experience as an Exercise Physiologist. I would like the cards to look professional but not boring and can be a little different to stand out when sitting with other Allied Health Professional cards.

Target Market(s)

GP's, Allied health practitioners, people with injuries wanting to exercise

Industry/Entity Type

Health And Wellness

Contact Information for Business Card

Megan Dorrit - Exercise Physiologist 0437 582 906
14 Larkspur Bend Rd
Bramwell Heights
(Gate 2, Brannock Fitness)
vantorahealth@maildrop-example.com
socialpage-example.com/Vantora

Requirements
Must have
• I would like to include a section to add next appointment date and time space to the back of the card.
Nice to have
• Rounded corners and a black background on 1 or 2 sides.
Should not have
• Pictures of fit/toned bodies etc

```html
<!DOCTYPE html>
<html lang="en">
<head>
<meta charset="utf-8">
<title>Vantora – Business Cards</title>
<link rel="stylesheet" href="https://fonts.googleapis.com/css2?family=Open+Sans:wght@400;600;700&display=swap">
<style>
  :root {
    --stage: #3a3a3c;
    --card-white: #ffffff;
    --brand-blue: #2f6bc4;
    --brand-blue-dark: #1f55a8;
    --brand-blue-light: #5aa6dc;
    --ink-grey: #555b63;
    --rule: #3b3b3b;
  }
  * { box-sizing: border-box; margin: 0; padding: 0; }
  html, body { width: 1200px; height: 896px; overflow: hidden; }
  body {
    background: var(--stage);
    font-family: "Open Sans", Arial, sans-serif;
    display: flex;
    align-items: center;
    justify-content: center;
    gap: 60px;
  }
  .card {
    position: relative;
    width: 520px;
    height: 300px;
    border-radius: 22px;
    overflow: hidden;
    box-shadow: 0 10px 30px rgba(0,0,0,.45);
  }

  /* Back: appointment card */
  .card--back { background: var(--card-white); }
  .card--back .brand {
    position: absolute; left: 44px; top: 62px;
    display: flex; align-items: center; gap: 12px;
  }
  .brand__dot {
    width: 46px; height: 46px; border-radius: 50%;
    background: var(--brand-blue-light);
  }
  .brand__name {
    font-size: 40px; font-weight: 600; color: var(--brand-blue);
    letter-spacing: .5px; line-height: 1;
  }
  .appointment {
    position: absolute; left: 44px; top: 150px; right: 44px;
  }
  .appointment__title {
    font-size: 19px; font-weight: 600; color: var(--brand-blue);
    margin-bottom: 18px;
  }
  .appointment__row {
    display: flex; align-items: flex-end; gap: 10px;
    font-size: 17px; color: var(--ink-grey);
    margin-bottom: 22px;
  }
  .appointment__line {
    flex: 1; border-bottom: 1px solid var(--rule); height: 1px; margin-bottom: 5px;
  }

  /* Front: contact card */
  .card--front {
    background: linear-gradient(135deg, #3d7fd6 0%, var(--brand-blue) 45%, var(--brand-blue-dark) 100%);
  }
  .card--front .swoosh {
    position: absolute; inset: 0; width: 100%; height: 100%;
  }
  .card--front .brand {
    position: absolute; left: 290px; top: 72px;
    display: flex; align-items: center; gap: 12px;
  }
  .card--front .brand__dot { width: 42px; height: 42px; }
  .card--front .brand__name { font-size: 36px; }
  .contact {
    position: absolute; left: 36px; bottom: 30px;
    color: #ffffff;
  }
  .contact__name { font-size: 24px; font-weight: 700; line-height: 1.15; }
  .contact__role { font-size: 15px; margin-bottom: 12px; }
  .contact__address { font-size: 14px; line-height: 1.35; margin-bottom: 10px; }
  .contact__list { list-style: none; font-size: 14px; line-height: 1.45; }
  .contact__list li { display: flex; align-items: center; gap: 8px; }
  .contact__list svg { width: 11px; height: 11px; flex: none; }
</style>
</head>
<body>

  <section class="card card--back" aria-label="Appointment side">
    <div class="brand">
      <span class="brand__dot"></span>
      <span class="brand__name">Vantora</span>
    </div>
    <div class="appointment">
      <p class="appointment__title">Next appointment</p>
      <div class="appointment__row"><span>Date</span><span class="appointment__line"></span></div>
      <div class="appointment__row"><span>Time</span><span class="appointment__line"></span></div>
    </div>
  </section>

  <section class="card card--front" aria-label="Contact side">
    <svg class="swoosh" viewBox="0 0 520 300" preserveAspectRatio="none" aria-hidden="true">
      <circle cx="388" cy="26" r="176" fill="var(--brand-blue-light)"/>
      <circle cx="390" cy="20" r="170" fill="#ffffff"/>
    </svg>
    <div class="brand">
      <span class="brand__dot"></span>
      <span class="brand__name">Vantora</span>
    </div>
    <div class="contact">
      <p class="contact__name">Megan Dorrit</p>
      <p class="contact__role">Exercise Physiologist</p>
      <p class="contact__address">14 Larkspur Bend Rd<br>Bramwell Heights</p>
      <ul class="contact__list">
        <li>
          <svg viewBox="0 0 12 12"><path d="M3 1 L5 3.5 L4 5 Q5.5 7.5 7 8 L8.5 7 L11 9 L9.5 11 Q4 10.5 1 3 Z" fill="#fff"/></svg>
          0437 582 906
        </li>
        <li>
          <svg viewBox="0 0 12 12"><rect x="1" y="2.5" width="10" height="7" fill="none" stroke="#fff" stroke-width="1.2"/><path d="M1 2.5 L6 6.5 L11 2.5" fill="none" stroke="#fff" stroke-width="1.2"/></svg>
          info@vantora-example.com
        </li>
        <li>
          <svg viewBox="0 0 12 12"><circle cx="6" cy="6" r="5" fill="none" stroke="#fff" stroke-width="1.2"/><path d="M1 6 H11 M6 1 Q3 6 6 11 Q9 6 6 1" fill="none" stroke="#fff" stroke-width="1"/></svg>
          www.vantora-example.com
        </li>
      </ul>
    </div>
  </section>

</body>
</html>
```